Business Card design for Property Developer

We need a business card design for a Melbourne based Property Developer called "Kestrel Grove Pty Ltd".

We subdivide land and onsell to builders etc.

We already have a company logo, which is attached. Also I have attached the layout requirements from the printer. We would like a 2-sided design with one side displaying our logo by itself and the other with the required info, such as name, address, tel no., email, abn etc. The card will need to be used by 4 members of staff so name and contact details should be interchangable.
Updates

If possible, can you please write "name' "job position" "phone" "email" "address" on the card but leave them so I can add the details at a later time. Thank you. Also I plan on printing with UV spot printing as a background on the card. Keep this is mind when designing.

Thanks again.

Hello designers, please do not include pics of houses, house plansĀ or construction machinery etc as we really do not like the way it looks. Thank you.

Target Market(s)

Real Estate Agents, Land Owners, Local Council Departments, Govt Bodies, other Developers etc.

Industry/Entity Type

Business

Requirements
Must have
• 2-sided design with one side displaying our logo by itself and the other with the required info, such as name, address, tel no., email, abn etc.

```html
<!DOCTYPE html>
<html lang="en">
<head>
<meta charset="utf-8">
<title>Kestrel Grove – Business Card</title>
<link href="https://fonts.googleapis.com/css2?family=Arimo:wght@400;700&display=swap" rel="stylesheet">
<style>
  :root {
    --page: #e6e6e6;
    --card-white: #ffffff;
    --card-fade: #e9e9e9;
    --brand-red: #b50f12;
    --brand-blue: #1f6fc4;
    --ink: #1b1b1b;
    --rule: #3a3a3a;
    --band-dark: #1e1e1e;
    --silver-light: #e2e2e2;
    --silver-mid: #a9a9a9;
  }
  * { box-sizing: border-box; margin: 0; padding: 0; }
  html, body { width: 1200px; height: 895px; overflow: hidden; }
  body {
    background: var(--page);
    font-family: "Arimo", Arial, sans-serif;
    position: relative;
  }
  .card {
    position: absolute;
    top: 302px;
    width: 568px;
    height: 342px;
    border-radius: 14px;
    overflow: hidden;
    background: radial-gradient(ellipse at 50% 25%, var(--card-white) 0%, var(--card-fade) 85%);
    display: flex;
    flex-direction: column;
  }
  .card--front { left: 18px; }
  .card--back { left: 612px; }
  .card__face { position: relative; height: 266px; }
  .card__bands { flex: 1; display: flex; flex-direction: column; }
  .band-line { height: 9px; background: var(--band-dark); }
  .band-silver {
    height: 22px;
    background: linear-gradient(90deg, var(--silver-mid), var(--silver-light) 50%, var(--silver-mid));
  }
  .band-thin { height: 3px; background: var(--band-dark); }
  .band-base {
    flex: 1;
    background: radial-gradient(ellipse at 50% 0%, #8e8e8e 0%, #3c3c3c 55%, #1a1a1a 100%);
  }

  /* Front */
  .brand-front {
    position: absolute;
    left: 0; right: 0; top: 62px;
    display: flex; flex-direction: column; align-items: center;
  }
  .brand-dot {
    width: 104px; height: 104px; border-radius: 50%;
    background: var(--brand-blue);
  }
  .brand-name {
    font-weight: 700;
    color: var(--brand-red);
    text-transform: uppercase;
    letter-spacing: 1px;
  }
  .brand-front .brand-name { font-size: 38px; margin-top: 22px; }

  /* Back */
  .brand-back {
    position: absolute; left: 30px; top: 128px;
    width: 124px;
    display: flex; flex-direction: column; align-items: center;
  }
  .brand-back .brand-dot { width: 44px; height: 44px; }
  .brand-back .brand-name { font-size: 13px; margin-top: 9px; letter-spacing: 0.3px; white-space: nowrap; }
  .divider {
    position: absolute; left: 173px; top: 103px;
    width: 1px; height: 123px; background: var(--rule);
  }
  .contact { position: absolute; left: 200px; top: 114px; color: var(--ink); }
  .contact__name { font-size: 17px; font-weight: 700; color: var(--brand-red); margin-left: 20px; }
  .contact__web { font-size: 12.5px; margin: 5px 0 0 20px; }
  .contact__row { display: flex; align-items: center; height: 14px; }
  .contact__row svg { width: 14px; height: 12px; margin-right: 6px; fill: var(--brand-red); }
  .contact__email { font-size: 12.5px; margin-top: 1px; }
  .contact__phone { font-size: 15px; letter-spacing: 0.3px; }
  .tagline {
    position: absolute; right: 34px; top: 246px;
    font-size: 9px; letter-spacing: 4.5px; color: var(--ink);
  }
</style>
</head>
<body>
  <section class="card card--front" aria-label="Card front">
    <div class="card__face">
      <div class="brand-front">
        <div class="brand-dot"></div>
        <div class="brand-name">Kestrel Grove</div>
      </div>
    </div>
    <div class="card__bands">
      <div class="band-line"></div><div class="band-silver"></div><div class="band-thin"></div><div class="band-base"></div>
    </div>
  </section>

  <section class="card card--back" aria-label="Card back">
    <div class="card__face">
      <div class="brand-back">
        <div class="brand-dot"></div>
        <div class="brand-name">Kestrel Grove</div>
      </div>
      <div class="divider"></div>
      <div class="contact">
        <p class="contact__name">John Doe</p>
        <p class="contact__web">www.kestrelgrove.com.au</p>
        <div class="contact__row contact__email">
          <svg viewBox="0 0 14 12"><path d="M0 4 7 0l7 4v8H0z"/><path d="M1 4.5 7 8l6-3.5" fill="none" stroke="#fff" stroke-width="1"/></svg>
          <span>jdoe@kestrelgrove.com.au</span>
        </div>
        <div class="contact__row contact__phone">
          <svg viewBox="0 0 14 12"><rect x="3" y="0" width="8" height="4"/><rect x="0" y="4" width="14" height="5"/><rect x="3" y="8" width="8" height="4"/></svg>
          <span>123 456 7890</span>
        </div>
        <div class="contact__row contact__phone">
          <svg viewBox="0 0 14 12"><path d="M0 3q7-4 14 0v2h-3V3.5H3V5H0z"/><rect x="2" y="6" width="10" height="6" rx="1"/></svg>
          <span>123 456 7890</span>
        </div>
        <div class="contact__row contact__phone">
          <svg viewBox="0 0 14 12"><rect x="0" y="0" width="14" height="12" rx="1"/><rect x="2" y="2" width="10" height="3" fill="#fff"/></svg>
          <span>123 456 7890</span>
        </div>
      </div>
      <p class="tagline">lorem ipsum dolor sit amet</p>
    </div>
    <div class="card__bands">
      <div class="band-line"></div><div class="band-silver"></div><div class="band-thin"></div><div class="band-base"></div>
    </div>
  </section>
</body>
</html>
```